FinTech company looking to revamp and expand client-facing interface for our financial models

Halvern Ledgerworks currently has a very simple website that allows clients to interact with our financial models. We are looking to completely redesign the current site and add several extra pages to provide extra functionality. We want the design to have a modern, slick feel, that will work on both a desktop or a tablet. It should be straightforward for clients to move between different pages at any time, and clear from the layout how to interact with the more advanced features. We have included screenshots of existing pages in the attached design brief, as well as sketches of the functionality required by the new pages, but can't provide a direct link to the current site.
Target Market(s)
Professional investors that will be paying to access the interface
Industry/Entity Type
Finance
Number of Pages Required
4 page
Colors
Designer to choose colors to be used in the design.
Look and feel
Each slider illustrates characteristics of the customer's brand and the style your logo design should communicate.

```html
<!DOCTYPE html>
<html lang="en">
<head>
<meta charset="utf-8">
<title>Halvern Ledgerworks — Models</title>
<link href="https://fonts.googleapis.com/css2?family=Roboto:wght@400;500&display=swap" rel="stylesheet">
<style>
  :root {
    --page-bg: #f7f7f8;
    --header-bg: #ffffff;
    --accent: #2f8fdd;
    --ink: #2f3338;
    --muted: #8b96a2;
    --row-alt: #f5f8fc;
    --head-bg: #f6f9fc;
    --filter-bg: #f6cd6b;
    --star-off: #b9c0c8;
    --star-on: #ef4b4b;
  }
  * { box-sizing: border-box; margin: 0; padding: 0; }
  html, body { width: 1200px; height: 676px; overflow: hidden; }
  body {
    position: relative;
    background: var(--page-bg);
    font-family: "Roboto", sans-serif;
    color: var(--ink);
  }
  .topbar {
    position: absolute; left: 0; top: 0; width: 1200px; height: 67px;
    background: var(--header-bg);
    box-shadow: 0 2px 8px rgba(0,0,0,0.03);
  }
  .brand {
    position: absolute; left: 150px; top: 18px;
    font-size: 23px; font-weight: 500; letter-spacing: 0.5px; color: var(--ink);
  }
  .horizon { position: absolute; top: 0; height: 67px; font-size: 12.5px; line-height: 67px; text-align: center; color: var(--ink); }
  .horizon.active { background: var(--accent); color: #fff; }
  .nav-item {
    position: absolute; top: 0; height: 67px; display: flex; align-items: center; gap: 7px;
    font-size: 13px; color: var(--ink);
  }
  .nav-item svg { width: 17px; height: 17px; }
  .nav-item.current { color: var(--accent); }
  .nav-underline { position: absolute; left: 538px; top: 65px; width: 93px; height: 2px; background: var(--accent); }

  .filter-tab {
    position: absolute; left: 0; top: 126px; width: 34px; height: 82px;
    background: var(--filter-bg); border-radius: 0 3px 3px 0;
  }
  .filter-tab span {
    position: absolute; left: 9px; top: 45px; transform: rotate(-90deg); transform-origin: left top;
    font-size: 11px; font-weight: 500; color: var(--ink);
  }
  .filter-tab svg { position: absolute; left: 9px; top: 52px; width: 15px; height: 15px; }

  .export {
    position: absolute; left: 1001px; top: 104px; display: flex; align-items: center; gap: 3px;
    font-size: 10.5px; font-weight: 500; color: var(--accent);
  }
  .export svg { width: 11px; height: 11px; }

  .models-table {
    position: absolute; left: 150px; top: 126px; width: 900px;
    border-radius: 4px; overflow: hidden; background: #fff;
    box-shadow: 0 3px 10px rgba(40,60,90,0.04);
  }
  .row {
    display: grid;
    grid-template-columns: 92px 82px 89px 81px 70px 68px 68px 72px 72px 69px 67px 70px;
    align-items: center; height: 70px; font-size: 13px;
  }
  .row.head { height: 46px; background: var(--head-bg); color: var(--muted); font-weight: 500; font-size: 12.5px; }
  .row:nth-child(odd):not(.head) { background: var(--row-alt); }
  .row > div { white-space: nowrap; }
  .id-cell { padding-left: 10px; display: flex; align-items: center; gap: 6px; }
  .head .id-cell { padding-left: 14px; gap: 4px; }
  .id-cell svg { width: 9px; height: 9px; }
  .time-cell { line-height: 16px; }
</style>
</head>
<body>
  <header class="topbar">
    <div class="brand">LEDGRA</div>
    <div class="horizon active" style="left:262px;width:60px;">250D</div>
    <div class="horizon" style="left:332px;width:40px;">83D</div>
    <div class="horizon" style="left:390px;width:40px;">42D</div>

    <div class="nav-item current" style="left:551px;">
      <svg viewBox="0 0 20 20" fill="none" stroke="currentColor" stroke-width="1.5"><path d="M2 9.5L10 2.5l8 7M4.5 7.5V17.5h11V7.5"/></svg>Models
    </div>
    <div class="nav-item" style="left:657px;">
      <svg viewBox="0 0 20 20" fill="none" stroke="currentColor" stroke-width="1.5"><circle cx="3.5" cy="3.5" r="1.8"/><circle cx="10" cy="3.5" r="1.8"/><circle cx="16.5" cy="3.5" r="1.8"/><circle cx="3.5" cy="10" r="1.8"/><circle cx="10" cy="10" r="1.8"/><circle cx="16.5" cy="10" r="1.8"/><circle cx="10" cy="16.5" r="1.8"/></svg>Portfolio Builder
    </div>
    <div class="nav-item" style="left:816px;">
      <svg viewBox="0 0 20 20" fill="none" stroke="currentColor" stroke-width="1.6"><path d="M10 3L2 7.5 10 12l8-4.5z"/><path d="M2 11.5L10 16l8-4.5"/></svg>Sensitivities
    </div>
    <div class="nav-item" style="left:953px;">
      <svg viewBox="0 0 20 20" fill="none" stroke="currentColor" stroke-width="1.5"><path d="M10 1.8l2.5 5.3 5.8.7-4.3 4 1.1 5.7L10 14.7l-5.1 2.8 1.1-5.7-4.3-4 5.8-.7z"/></svg>Favourites
    </div>
    <div class="nav-underline"></div>
  </header>

  <aside class="filter-tab">
    <span>Filter</span>
    <svg viewBox="0 0 16 16" fill="none" stroke="#2f3338" stroke-width="1.3"><rect x="1.5" y="6" width="5" height="8.5" rx="2"/><rect x="9.5" y="6" width="5" height="8.5" rx="2"/><path d="M3 6V2.5h2V6M11 6V2.5h2V6M6.5 9h3"/></svg>
  </aside>

  <div class="export">
    <svg viewBox="0 0 12 12" fill="none" stroke="currentColor" stroke-width="1.4"><path d="M5 2H2v8h8V7M7 1.5h3.5V5M10.5 1.5L5.5 6.5"/></svg>Export
  </div>

  <section class="models-table">
    <div class="row head">
      <div class="id-cell">ID <svg viewBox="0 0 10 10" fill="none" stroke="currentColor" stroke-width="1.4"><path d="M2.5 4l2.5 2.5L7.5 4"/></svg></div>
      <div>Sector</div><div>Time</div><div>Quality</div><div>Stat 1</div><div>Stat 2</div><div>Stat 3</div><div>Stat 4</div><div>Stat 5</div><div>Stat 6</div><div>Stat 7</div><div>Stat 8</div>
    </div>

    <div class="row">
      <div class="id-cell"><svg viewBox="0 0 10 10" fill="none" stroke="var(--star-off)" stroke-width="0.8"><path d="M5 .8l1.2 2.6 2.9.3-2.2 2 .6 2.9L5 7.2 2.5 8.6l.6-2.9-2.2-2 2.9-.3z"/></svg>Model 1</div>
      <div>Materials</div><div class="time-cell">2019-07-03<br>12:15:00.000</div><div>30.2888</div><div>2.01574</div><div>23.305</div><div>-0.149368</div><div>22.3054</div><div>4.63714</div><div>0.945706</div><div>2.81949</div><div>2.60858</div>
    </div>
    <div class="row">
      <div class="id-cell"><svg viewBox="0 0 10 10" fill="var(--star-on)"><path d="M5 .8l1.2 2.6 2.9.3-2.2 2 .6 2.9L5 7.2 2.5 8.6l.6-2.9-2.2-2 2.9-.3z"/></svg>Model 2</div>
      <div>Materials</div><div class="time-cell">2019-07-03<br>12:15:00.000</div><div>30.2888</div><div>2.01574</div><div>23.305</div><div>-0.149368</div><div>22.3054</div><div>4.63714</div><div>0.945706</div><div>2.81949</div><div>2.60858</div>
    </div>
    <div class="row">
      <div class="id-cell"><svg viewBox="0 0 10 10" fill="none" stroke="var(--star-off)" stroke-width="0.8"><path d="M5 .8l1.2 2.6 2.9.3-2.2 2 .6 2.9L5 7.2 2.5 8.6l.6-2.9-2.2-2 2.9-.3z"/></svg>Model 3</div>
      <div>Materials</div><div class="time-cell">2019-07-03<br>12:15:00.000</div><div>30.2888</div><div>2.01574</div><div>23.305</div><div>-0.149368</div><div>22.3054</div><div>4.63714</div><div>0.945706</div><div>2.81949</div><div>2.60858</div>
    </div>
    <div class="row">
      <div class="id-cell"><svg viewBox="0 0 10 10" fill="none" stroke="var(--star-off)" stroke-width="0.8"><path d="M5 .8l1.2 2.6 2.9.3-2.2 2 .6 2.9L5 7.2 2.5 8.6l.6-2.9-2.2-2 2.9-.3z"/></svg>Model 4</div>
      <div>Materials</div><div class="time-cell">2019-07-03<br>12:15:00.000</div><div>30.2888</div><div>2.01574</div><div>23.305</div><div>-0.149368</div><div>22.3054</div><div>4.63714</div><div>0.945706</div><div>2.81949</div><div>2.60858</div>
    </div>
    <div class="row">
      <div class="id-cell"><svg viewBox="0 0 10 10" fill="none" stroke="var(--star-off)" stroke-width="0.8"><path d="M5 .8l1.2 2.6 2.9.3-2.2 2 .6 2.9L5 7.2 2.5 8.6l.6-2.9-2.2-2 2.9-.3z"/></svg>Model 5</div>
      <div>Materials</div><div class="time-cell">2019-07-03<br>12:15:00.000</div><div>30.2888</div><div>2.01574</div><div>23.305</div><div>-0.149368</div><div>22.3054</div><div>4.63714</div><div>0.945706</div><div>2.81949</div><div>2.60858</div>
    </div>
    <div class="row">
      <div class="id-cell"><svg viewBox="0 0 10 10" fill="none" stroke="var(--star-off)" stroke-width="0.8"><path d="M5 .8l1.2 2.6 2.9.3-2.2 2 .6 2.9L5 7.2 2.5 8.6l.6-2.9-2.2-2 2.9-.3z"/></svg>Model 6</div>
      <div>Materials</div><div class="time-cell">2019-07-03<br>12:15:00.000</div><div>30.2888</div><div>2.01574</div><div>23.305</div><div>-0.149368</div><div>22.3054</div><div>4.63714</div><div>0.945706</div><div>2.81949</div><div>2.60858</div>
    </div>
  </section>
</body>
</html>
```